Quilvo Garage Doors Business Card

I need a Business Card for my garage door business:
Quilvo Garage Doors.
please add:
logo
phone number: 855-3-QUILVO
(853-392)

email: service@quilvogaragedoors.com
website: www.quilvogaragedoors.com

The attached image is recommendation ONLY.

```html
<!DOCTYPE html>
<html lang="en">
<head>
<meta charset="utf-8">
<title>Quilvo Garage Doors – Business Card</title>
<link rel="stylesheet" href="https://fonts.googleapis.com/css2?family=Montserrat:wght@400;500;700&family=Varela+Round&display=swap">
<style>
  :root {
    --teal: #5cc8cc;
    --teal-dark: #3fb0b5;
    --ink: #1d1d1f;
    --grey-line: #4a4a4a;
    --card-white: #f7f7f6;
    --backdrop: #e9e6e1;
    --photo-green: #6f7d4a;
    --photo-light: #b7bda6;
  }
  * { margin: 0; padding: 0; box-sizing: border-box; }
  html, body { width: 1200px; height: 780px; overflow: hidden; }
  body {
    background: var(--backdrop);
    position: relative;
    font-family: "Montserrat", Arial, sans-serif;
  }
  .card {
    position: absolute;
    top: 235px;
    width: 540px;
    height: 309px;
    border-radius: 4px;
    overflow: hidden;
    box-shadow: 0 10px 26px rgba(0,0,0,.18);
  }

  /* Front card */
  .card-front { left: 40px; background: var(--card-white); }
  .front-band {
    position: absolute; left: 0; right: 0; bottom: 0; height: 70px;
    background: linear-gradient(180deg, var(--teal) 0%, var(--teal-dark) 100%);
  }
  .front-rule {
    position: absolute; left: 0; right: 0; bottom: 76px; height: 2px;
    background: var(--grey-line);
  }
  .front-mark {
    position: absolute; left: 38px; bottom: 36px; width: 80px; height: 80px;
    border-radius: 50%; background: var(--teal); border: 6px solid #e6f6f6;
  }
  .wordmark {
    position: absolute; left: 150px; top: 26px;
    font-family: "Varela Round", Arial, sans-serif;
    font-weight: 400;
    color: var(--ink); font-size: 32px; line-height: 1.05;
  }
  .employee { position: absolute; left: 150px; top: 108px; }
  .employee-name { font-weight: 700; font-size: 16px; color: var(--ink); letter-spacing: .2px; }
  .employee-title { font-size: 13px; color: var(--teal); margin-top: 1px; }
  .contacts { position: absolute; left: 150px; top: 158px; list-style: none; }
  .contacts li {
    display: flex; align-items: center; gap: 8px;
    font-size: 12.5px; color: var(--ink); height: 20px;
  }
  .contacts svg { width: 15px; height: 15px; flex: none; }

  /* Back card */
  .card-back { left: 620px; background: var(--photo-green); }
  .back-photo {
    position: absolute; inset: 0 0 44px 0;
    background: linear-gradient(120deg, #4d5a33 0%, var(--photo-green) 45%, var(--photo-light) 100%);
  }
  .back-panel {
    position: absolute; top: 0; right: 0; bottom: 44px; width: 200px;
    background: rgba(255,255,255,.45);
    display: flex; flex-direction: column; align-items: center; justify-content: center; gap: 18px;
  }
  .back-mark { width: 64px; height: 64px; border-radius: 50%; background: var(--teal); }
  .back-wordmark {
    font-family: "Varela Round", Arial, sans-serif;
    color: #ffffff; font-size: 26px; line-height: 1.1; text-align: center;
  }
  .back-strip {
    position: absolute; left: 0; right: 0; bottom: 0; height: 44px;
    background: var(--teal);
    display: flex; align-items: center; padding-left: 28px;
    font-size: 15px; color: var(--ink); font-weight: 500;
  }
</style>
</head>
<body>

<section class="card card-front">
  <div class="front-rule"></div>
  <div class="front-band"></div>
  <div class="front-mark"></div>
  <h1 class="wordmark">Quilvo<br>Garage Doors</h1>
  <div class="employee">
    <p class="employee-name">EMPLOYEE NAME</p>
    <p class="employee-title">Managing Director</p>
  </div>
  <ul class="contacts">
    <li>
      <svg viewBox="0 0 16 16"><rect width="16" height="16" fill="var(--teal)"/><path d="M5 3.5c.6 0 1.2 1.6 1.2 2.1 0 .5-.8.8-.6 1.3.4 1 1.4 2 2.4 2.4.5.2.8-.6 1.3-.6.5 0 2.1.6 2.1 1.2 0 1-1 1.8-2 1.6C6.4 11 4.9 9.6 4 6.6c-.3-1.1.4-3.1 1-3.1z" fill="var(--ink)"/></svg>
      855-3-QUILVO (853-392)
    </li>
    <li>
      <svg viewBox="0 0 16 16"><rect width="16" height="16" fill="var(--teal)"/><rect x="3" y="4.5" width="10" height="7" fill="none" stroke="var(--ink)" stroke-width="1.3"/><path d="M3 4.5l5 4 5-4" fill="none" stroke="var(--ink)" stroke-width="1.3"/></svg>
      service@quilvogaragedoors.com
    </li>
    <li>
      <svg viewBox="0 0 16 16"><rect width="16" height="16" fill="var(--teal)"/><circle cx="8" cy="8" r="5" fill="none" stroke="var(--ink)" stroke-width="1.2"/><ellipse cx="8" cy="8" rx="2.2" ry="5" fill="none" stroke="var(--ink)" stroke-width="1"/><path d="M3 8h10" stroke="var(--ink)" stroke-width="1"/></svg>
      www.quilvogaragedoors.com
    </li>
  </ul>
</section>

<section class="card card-back">
  <div class="back-photo" role="img" aria-label="Team photo: staff in uniform standing beside a branded service van in front of trees"></div>
  <div class="back-panel">
    <div class="back-mark"></div>
    <p class="back-wordmark">Quilvo<br>Garage Doors</p>
  </div>
  <div class="back-strip">www.quilvogaragedoors.com</div>
</section>

</body>
</html>
```